Re-design of website

I have an existing website that I would like to improve. The functionality will remain the same but the overall look will need to be changed. I have some ideas of what i would like included and am also in need of someone else to input their own creative ideas. I am on a tight deadline to get these improvements made as I have many people being directed to the site via our advertising campaigns that are in full swing late next week. Thanks
Target Market(s)
The website provides a virtual space for families to learn more about our learning program which we operate out of Dubai and will soon spread to the other Emirates. The families are generally between 25-50 year old parents with children up to the age of 6. They are local Emirati's as well as expats.

```html
<!DOCTYPE html>
<html lang="en">
<head>
<meta charset="utf-8">
<title>Bright Sprouts — Whole Brain Training</title>
<link rel="stylesheet" href="https://fonts.googleapis.com/css2?family=Arimo:ital,wght@0,400;0,700;1,700&display=swap">
<style>
  :root {
    --page-bg: #efefeb;
    --ink: #333333;
    --ink-soft: #555555;
    --muted: #8a8a8a;
    --accent: #f07a22;
    --leaf: #6f9a1c;
    --leaf-dark: #5d8614;
    --rule: #d9d9d4;
    --band: #d8d8d5;
    --card: #ffffff;
    --star: #7d6fb8;
    --white: #ffffff;
  }
  * { box-sizing: border-box; margin: 0; padding: 0; }
  html, body { width: 1200px; height: 1000px; overflow: hidden; }
  body {
    background: var(--page-bg);
    font-family: "Arimo", Arial, sans-serif;
    color: var(--ink);
    position: relative;
  }

  /* Header */
  .site-header { position: absolute; left: 0; top: 0; width: 1200px; height: 250px; }
  .header-ornament {
    position: absolute; left: 455px; top: 28px; width: 290px; height: 66px;
    background: radial-gradient(ellipse at center, #7fa82a 0%, #6f9a1c 55%, rgba(111,154,28,0.35) 100%);
    border-radius: 40px 40px 14px 14px;
  }
  .header-rule { position: absolute; left: 410px; width: 380px; height: 1px; background: var(--rule); }
  .header-rule--top { top: 104px; }
  .header-rule--bottom { top: 176px; }
  .brand-name {
    position: absolute; left: 0; top: 122px; width: 1200px; text-align: center;
    font-size: 34px; font-weight: 700; letter-spacing: 0.5px; color: var(--ink);
  }
  .main-nav {
    position: absolute; left: 0; top: 202px; width: 1200px;
    display: flex; justify-content: center; gap: 52px;
    list-style: none; font-size: 17px; color: var(--ink-soft);
  }
  .main-nav li { display: flex; align-items: center; gap: 7px; }
  .main-nav .is-current { color: var(--accent); }
  .main-nav svg { width: 16px; height: 15px; }

  /* Hero */
  .hero {
    position: absolute; left: 0; top: 250px; width: 1200px; height: 285px;
    background: linear-gradient(180deg, var(--leaf) 0%, var(--leaf-dark) 100%);
  }
  .hero-photo {
    position: absolute; left: 70px; top: 0; width: 330px; height: 285px;
    background: linear-gradient(90deg, #9a9a9a 0%, #cfcfcf 45%, #bdbdbd 75%, rgba(111,154,28,0) 100%);
  }
  .hero-copy {
    position: absolute; right: 205px; top: 78px; width: 420px; text-align: right;
    text-transform: uppercase; line-height: 1;
  }
  .hero-copy .line-dark { color: #111; font-size: 20px; }
  .hero-copy .line-light { color: var(--white); font-size: 28px; }
  .hero-copy .line-first { font-size: 30px; margin-right: 78px; }
  .hero-copy p { margin-bottom: 4px; }
  .hero-copy .hero-note {
    text-transform: none; font-size: 10.5px; color: #111; line-height: 1.7;
    margin-top: 14px; margin-right: 0; text-align: right;
  }
  .hero-copy .hero-cta { color: #111; font-size: 15px; margin-top: 6px; }

  /* Intro */
  .intro { position: absolute; left: 0; top: 535px; width: 1200px; height: 245px; }
  .intro-heading {
    position: absolute; left: 180px; top: 42px;
    font-size: 14px; font-style: italic; font-weight: 700; color: var(--ink);
  }
  .intro-text {
    position: absolute; left: 180px; top: 76px; width: 670px;
    font-size: 11.5px; line-height: 1.9; color: var(--muted);
  }
  .intro-figure {
    position: absolute; left: 905px; top: 22px; width: 84px; height: 205px;
    background: linear-gradient(180deg, #b9b4ac 0%, #e6e3dd 30%, #dcd8d0 85%, #9d978d 100%);
    border-radius: 30px 30px 8px 8px;
  }

  /* Feedback */
  .feedback { position: absolute; left: 160px; top: 790px; width: 880px; height: 210px; background: var(--band); }
  .feedback-rule { position: absolute; left: 0; top: 0; width: 880px; height: 3px; background: var(--accent); }
  .feedback-notch { position: absolute; left: 432px; top: 3px; width: 16px; height: 9px; }
  .feedback-title {
    position: absolute; left: 0; top: 34px; width: 880px; text-align: center;
    font-size: 13px; font-weight: 700; color: var(--ink); letter-spacing: 0.3px;
  }
  .feedback-cards { position: absolute; left: 80px; top: 78px; display: flex; gap: 30px; list-style: none; }
  .feedback-card { width: 160px; height: 122px; background: var(--card); padding: 8px; }
  .feedback-photo {
    width: 90px; height: 78px; margin: 0 auto;
    background: linear-gradient(180deg, #e9e9e9 0%, #c9c9c9 100%);
  }
  .feedback-caption { display: flex; justify-content: space-between; margin-top: 10px; font-size: 7.5px; color: var(--ink); text-transform: uppercase; }
  .feedback-stars { color: var(--star); font-size: 9px; letter-spacing: 1px; }
</style>
</head>
<body>

<header class="site-header">
  <div class="header-ornament" role="img" aria-label="Green floral scroll ornament"></div>
  <div class="header-rule header-rule--top"></div>
  <h1 class="brand-name">BRIGHT SPROUTS</h1>
  <div class="header-rule header-rule--bottom"></div>
  <ul class="main-nav">
    <li class="is-current">
      <svg viewBox="0 0 16 15" aria-hidden="true"><path d="M8 1 L15 7.5 H13 V14 H9.5 V10 H6.5 V14 H3 V7.5 H1 Z" fill="#333"/></svg>
      HOME
    </li>
    <li>ABOUT US</li>
    <li>SERVICES</li>
    <li>VECHICLES</li>
    <li>CONTACT US</li>
  </ul>
</header>

<section class="hero">
  <div class="hero-photo" role="img" aria-label="Black and white portrait photo of a young girl in a headscarf"></div>
  <div class="hero-copy">
    <p class="line-dark">We have</p>
    <p class="line-light line-first">First</p>
    <p class="line-dark">Whole brain training</p>
    <p class="line-light">Program</p>
    <p class="hero-note">designed to maximise your child's potential during<br>this key period of development.</p>
    <p class="hero-cta">Join us</p>
  </div>
</section>

<section class="intro">
  <h2 class="intro-heading">YOUR CHOICE EVEN WHAT IS OUR</h2>
  <p class="intro-text">Research and leading academics agree that the early years of a child's life defined as the 6 month old to 6 year old age group is a critical time period to enhance the emotional and intellectual IQ of a child. 80% of your child's brain is developed by the age of 6 years old, to not offer heightened stimulation and specifically, right brain training during this period means their child will not use a high proportion of their brain in their life time. Right brain training during this period means that your child will not use a high proportion of their brain in their life time.</p>
  <div class="intro-figure" role="img" aria-label="Photo of a boy standing in traditional white dress"></div>
</section>

<section class="feedback">
  <div class="feedback-rule"></div>
  <svg class="feedback-notch" viewBox="0 0 16 9" aria-hidden="true"><path d="M0 0 H16 L8 9 Z" fill="#f07a22"/></svg>
  <h2 class="feedback-title">OUR CLIENT FEEDBACK</h2>
  <ul class="feedback-cards">
    <li class="feedback-card">
      <div class="feedback-photo" role="img" aria-label="Photo of a client"></div>
      <div class="feedback-caption"><span>Amazing and good</span><span class="feedback-stars">★★★★★</span></div>
    </li>
    <li class="feedback-card">
      <div class="feedback-photo" role="img" aria-label="Photo of a client"></div>
      <div class="feedback-caption"><span>How can you believe</span><span class="feedback-stars">★★★★★</span></div>
    </li>
    <li class="feedback-card">
      <div class="feedback-photo" role="img" aria-label="Photo of a client"></div>
      <div class="feedback-caption"><span>This helped my son</span><span class="feedback-stars">★★★★★</span></div>
    </li>
    <li class="feedback-card">
      <div class="feedback-photo" role="img" aria-label="Photo of a client"></div>
      <div class="feedback-caption"><span>This helped my girl</span><span class="feedback-stars">★★★★★</span></div>
    </li>
  </ul>
</section>

</body>
</html>
```